Brochure Design Project

TGRP
The brochure is intended to be on Tarlow Guild of Restorative Practice website available for the members to download for the purpose of educating public about benefits of clinical hypnosis and introduce it as possible treatment option. There should be a empty space left on the last page for the member to stamp their office information.
So, the intended audience is general public that might be interested in hypnosis treatment
White on blue is logo of TGRP.
I would like the brochure to have bright complimentary colors with imagery that is used in health care/complimentary medicine - nature, relaxation, etc.
TGRP website is TGRPx.net.

```html
<!DOCTYPE html>
<html lang="en">
<head>
<meta charset="utf-8">
<title>TGRP Hypnosis Brochure</title>
<link href="https://fonts.googleapis.com/css2?family=Open+Sans:wght@400;600&family=Roboto+Condensed:wght@400;700&family=Tinos:wght@400;700&display=swap" rel="stylesheet">
<style>
:root{
  --navy:#10167f;
  --charcoal:#3b3b3d;
  --paper:#ffffff;
  --stage:#e9e9e9;
  --ink:#1e1e28;
}
*{box-sizing:border-box;margin:0;padding:0}
html,body{width:1173px;height:1200px;overflow:hidden;background:var(--stage)}
body{font-family:"Open Sans",sans-serif;color:var(--ink);position:relative}
.sheet{position:absolute;left:30px;width:1113px;height:560px;display:grid;grid-template-columns:repeat(3,371px);background:var(--paper);box-shadow:0 6px 18px rgba(0,0,0,.18)}
.sheet--outer{top:25px}
.sheet--inner{top:615px}
.panel{position:relative;height:560px;overflow:hidden}
.panel + .panel{border-left:1px solid #ececec}
.shapes,.photo{position:absolute;inset:0;width:371px;height:560px}
.band{position:absolute;left:0;right:0;bottom:0;height:16px;background:var(--navy)}
.copy{position:absolute;left:28px;right:28px;font-size:9.4px;line-height:1.38}
.copy p{margin-bottom:4px}
.heading{font-family:"Tinos",serif;font-weight:700;color:var(--navy);font-size:15px;margin-bottom:3px}
.heading--caps{font-size:17px;letter-spacing:.5px}
.heading--gap{margin-top:8px}
.brand{display:flex;align-items:center;gap:8px;font-family:"Tinos",serif;font-weight:700;color:var(--navy);font-size:34px;letter-spacing:4px}
.brand__square{width:18px;height:18px;background:var(--navy)}
.contact{position:absolute;left:0;right:0;top:385px;text-align:center}
.contact .brand{justify-content:center;margin-bottom:14px}
.contact__tag{font-size:14px;font-weight:600;color:#2a2a2a;line-height:1.3;margin-bottom:14px}
.contact__mail{font-size:13px;font-weight:600;margin-bottom:12px}
.contact__web{font-size:13px;letter-spacing:6px;font-weight:600}
.cover{position:absolute;right:26px;top:305px;text-align:right}
.cover .brand{justify-content:flex-end;margin-bottom:16px}
.cover__kicker{font-family:"Tinos",serif;font-weight:700;color:var(--navy);font-size:17px}
.cover__title{font-family:"Roboto Condensed",sans-serif;font-weight:700;color:var(--charcoal);font-size:31px;line-height:1.05}
.cover__title span{display:block;color:var(--navy);font-weight:400;font-size:36px}
.cover__web{font-size:12px;letter-spacing:6px;margin-top:8px}
.apps{list-style:none;font-size:9.4px;line-height:1.45;margin-bottom:18px}
.apps li::before{content:"•";color:var(--navy);margin-right:5px}
</style>
</head>
<body>

<section class="sheet sheet--outer">
  <article class="panel">
    <svg class="photo" viewBox="0 0 371 560" role="img" aria-label="Photo of a counsellor comforting an older client">
      <defs><linearGradient id="g1" x1="0" y1="0" x2="1" y2="1"><stop offset="0" stop-color="#8f9a6a"/><stop offset=".6" stop-color="#c9c2b0"/><stop offset="1" stop-color="#e6e0d6"/></linearGradient></defs>
      <polygon points="0,0 371,0 371,100 0,228" fill="url(#g1)"/>
    </svg>
    <svg class="shapes" viewBox="0 0 371 560" aria-hidden="true">
      <line x1="0" y1="228" x2="371" y2="100" stroke="var(--navy)" stroke-width="3"/>
      <polygon points="295,128 371,102 371,185" fill="var(--charcoal)"/>
    </svg>
    <div class="copy" style="top:238px">
      <h2 class="heading">What it is</h2>
      <p>Hypnosis is considered to be a state of focused attention and inner absorption; there is decreased awareness of surroundings and increased ability to respond to acceptable suggestions.</p>
      <p>A collaborative process that helps a person's mind and body function more comfortably and effectively. It is not uncommon for all of us to experience a situation when we are so preoccupied with a thought or experience that we neglect surroundings. Examples – watching a favorite show, computer games or driving under "highway" hypnosis.</p>
      <p>It requires special training to use hypnosis appropriately in medicine, dentistry and psychotherapy and should be done by licensed professionals in respected fields.</p>
      <h2 class="heading heading--gap">What it is not</h2>
      <p>It is not a mind control, just a suggestion. It cannot be imposed on an unwilling or uninterested person. It is not a miracle or cure, but a way to solve some problems.</p>
    </div>
    <div class="band"></div>
  </article>

  <article class="panel">
    <svg class="photo" viewBox="0 0 371 560" role="img" aria-label="Photo of a woman meditating on grass in a park">
      <defs><linearGradient id="g2" x1="0" y1="0" x2="0" y2="1"><stop offset="0" stop-color="#6f8f5a"/><stop offset="1" stop-color="#a8c47a"/></linearGradient></defs>
      <polygon points="0,0 371,0 371,160 0,140" fill="url(#g2)"/>
    </svg>
    <svg class="photo" viewBox="0 0 371 560" role="img" aria-label="Photo of stacked smooth stones fading to white">
      <defs><radialGradient id="g3" cx=".5" cy=".4" r=".6"><stop offset="0" stop-color="#8a8a8a"/><stop offset=".6" stop-color="#d6d6d6"/><stop offset="1" stop-color="#ffffff"/></radialGradient></defs>
      <rect x="60" y="170" width="250" height="190" fill="url(#g3)"/>
    </svg>
    <svg class="shapes" viewBox="0 0 371 560" aria-hidden="true">
      <line x1="0" y1="140" x2="371" y2="160" stroke="#111" stroke-width="3"/>
      <rect x="0" y="544" width="371" height="16" fill="var(--charcoal)"/>
    </svg>
    <div class="contact">
      <div class="brand"><span class="brand__square"></span>TGRP</div>
      <p class="contact__tag">Lorem Ipsum is not simply<br>random text</p>
      <p class="contact__mail">office@tgrpx-mail.net</p>
      <p class="contact__web">www.TGRPx.net</p>
    </div>
  </article>

  <article class="panel">
    <svg class="photo" viewBox="0 0 371 560" role="img" aria-label="Photo of a smiling doctor in a white coat with a stethoscope">
      <defs><linearGradient id="g4" x1="0" y1="0" x2="1" y2="0"><stop offset="0" stop-color="#e8eef2"/><stop offset=".6" stop-color="#f4f6f8"/><stop offset="1" stop-color="#9fd3e2"/></linearGradient></defs>
      <polygon points="0,0 371,0 371,270 0,190" fill="url(#g4)"/>
    </svg>
    <svg class="shapes" viewBox="0 0 371 560" aria-hidden="true">
      <line x1="0" y1="190" x2="371" y2="270" stroke="var(--navy)" stroke-width="3"/>
      <polygon points="0,192 120,218 0,290" fill="var(--charcoal)"/>
    </svg>
    <div class="cover">
      <div class="brand"><span class="brand__square"></span>TGRP</div>
      <p class="cover__kicker">WHAT, WHY, WHEN, HOW,</p>
      <h1 class="cover__title">AND COULD IT BE<span>RIGHT FOR ME?</span></h1>
      <p class="cover__web">www.TGRPx.net</p>
    </div>
    <div class="band"></div>
  </article>
</section>

<section class="sheet sheet--inner">
  <article class="panel">
    <svg class="photo" viewBox="0 0 371 560" role="img" aria-label="Photo of a couple consulting with a doctor">
      <defs><linearGradient id="g5" x1="0" y1="0" x2="1" y2="0"><stop offset="0" stop-color="#e9dccf"/><stop offset=".5" stop-color="#f3efe9"/><stop offset="1" stop-color="#dfe6ee"/></linearGradient></defs>
      <polygon points="0,0 371,0 371,205 0,145" fill="url(#g5)"/>
    </svg>
    <svg class="shapes" viewBox="0 0 371 560" aria-hidden="true">
      <line x1="0" y1="145" x2="371" y2="205" stroke="var(--navy)" stroke-width="3"/>
      <polygon points="0,147 105,164 0,205" fill="var(--charcoal)"/>
    </svg>
    <div class="copy" style="top:218px">
      <h2 class="heading">Why use hypnosis</h2>
      <p>Hypnosis is unique in its ability to help you unlock imagination, bypass the "can never happen" censor of the conscious mind, and simply help one see experiences and memories in a different light.</p>
      <p>It can help find solutions and resolutions to a difficult mental or physical problem, and find inner sources of strength and resilience.</p>
      <p>It can help a person better understand one's own as well as others' motivations and behavior.</p>
      <p>It allows a person to choose and develop abilities and capacities that can help achieve a desired goal.</p>
      <p>During the process of hypnosis a person is frequently taught how use individualized cues and techniques to achieve desired result (decrease anxiety, reduce pain, improve sport performance, etc.) With practice, a person can achieve a level of control that seemed impossible before.</p>
      <p>Hypnosis has been found to be very effective for treating many mental and physical conditions, as well improving physical and mental performance, and changing undesirable habits.</p>
    </div>
    <div class="band"></div>
  </article>

  <article class="panel">
    <svg class="shapes" viewBox="0 0 371 560" aria-hidden="true">
      <polygon points="0,470 180,458 0,560" fill="var(--charcoal)"/>
    </svg>
    <div class="copy" style="top:38px">
      <h2 class="heading">Its applications can include:</h2>
      <ul class="apps">
        <li>Anxiety disorders;</li>
        <li>Coping with emotional and physical trauma;</li>
        <li>Insomnia;</li>
        <li>Acute and chronic pain relief;</li>
        <li>Preparation for surgical procedures;</li>
        <li>Childbirth;</li>
        <li>Decreasing side effects of chemotherapy and radiation;</li>
        <li>Gastrointestinal disorders;</li>
        <li>Asthma;</li>
        <li>Sports performance and tests preparation;</li>
        <li>Fear of flying and</li>
        <li>Smoking cessation and weight control</li>
      </ul>
      <h2 class="heading heading--caps">HOW</h2>
      <p>A person conducting hypnosis will walk you through the process, help define goals and expectations, and explain how you can achieve the results you want. Hypnosis starts with an induction process: you simply concentrate on an object, idea or symbol. Induction is followed by relevant communication and crafting of the suggestion. The last step is reorientation and discussion of the experience, and instruction on home practice. All hypnosis is ultimately a form of self hypnosis.</p>
    </div>
  </article>

  <article class="panel">
    <svg class="photo" viewBox="0 0 371 560" role="img" aria-label="Photo of a person with raised arms silhouetted against a sunset sea">
      <defs><linearGradient id="g6" x1="0" y1="0" x2="0" y2="1"><stop offset="0" stop-color="#7f8fa3"/><stop offset=".45" stop-color="#d9c3a2"/><stop offset=".65" stop-color="#4a4f57"/><stop offset="1" stop-color="#2b2f36"/></linearGradient></defs>
      <polygon points="0,560 0,545 371,380 371,560" fill="url(#g6)"/>
    </svg>
    <svg class="shapes" viewBox="0 0 371 560" aria-hidden="true">
      <line x1="180" y1="455" x2="345" y2="380" stroke="var(--navy)" stroke-width="3"/>
    </svg>
    <div class="copy" style="top:38px;right:40px">
      <h2 class="heading">Is Hypnosis right for me?</h2>
      <p>Hypnosis is a wonderful and effective tool. If you are not familiar with hypnosis, you might worry about loss of control and embarrassment. People are also worried that their problems cannot be helped. Hypnosis might offer a novel way to approach or resolve the problem, or just see it in a different light.</p>
      <p>Even if hypnosis does not immediately solve the problem, you can still learn how to be a little more comfortable and experience a deeper level of physical and mental relaxation.</p>
      <p>Practice will help.</p>
      <p>Well-trained medical or mental health professionals will help you discover and use resources and strengths that you did not know you had.</p>
      <p>Your therapist, doctor or dentist might be the best person to discuss hypnosis and how it can be helpful to you. Licensed professionals get their training and certification through the Tarlow Guild of Restorative Practice. You can find a list of certified providers on TGRPx.net.</p>
    </div>
    <div class="band"></div>
  </article>
</section>

</body>
</html>
```